New Business card design to reflect rebrand

I would like a business card design with a good base colour for our new logo and also a placeholder for a profile pic of the card holder. the design needs to be editable to the point that we can easily change the picture of the person and use that design for printlarkly etc. we are looking at a metalic finish business card so will need a good base colour to bring out the finish.

Target Market(s)

prospective customers

Industry/Entity Type

Business

Contact Information for Business Card

I would like one editable design that we can change the name of the card holder and profile picture. The design need to be in a format that be send to printlarkly etc.

Our address is Fenwick Lodge, Mill Lane, Oakridge Wick, KT14 3WB Tel no. 01632 960418

Requirements
Must have
• place holder for a profile pic for the card holder. in AI or preferably PSD format

```html
<!DOCTYPE html>
<html lang="en">
<head>
<meta charset="utf-8">
<title>Brightwell Workplace Services – Business Card</title>
<link href="https://fonts.googleapis.com/css2?family=Arimo:wght@400;700&display=swap" rel="stylesheet">
<style>
  :root {
    --page-bg: #d9d9d9;
    --card-front: #fbfbfb;
    --card-front-edge: #ececec;
    --ink: #2b2b2b;
    --ink-soft: #3c3c3c;
    --icon-bg: #333333;
    --back-top: #3b3b3b;
    --back-bottom: #1f1f1f;
    --brand-blue: #5b7696;
    --brand-orange: #e2722f;
    --photo-ring: #3a3a3a;
    --photo-fill-a: #c9c9c9;
    --photo-fill-b: #5a5e66;
  }
  * { box-sizing: border-box; margin: 0; padding: 0; }
  html, body {
    width: 1200px; height: 900px; overflow: hidden;
    background: var(--page-bg);
    font-family: "Arimo", Arial, sans-serif;
  }
  .card-set {
    position: absolute; top: 170px; left: 250px;
    display: flex; gap: 60px;
  }
  .card {
    width: 320px; height: 560px; position: relative;
    box-shadow: 0 10px 30px rgba(0,0,0,.25);
  }
  /* Front */
  .card-front {
    background: linear-gradient(160deg, var(--card-front), var(--card-front-edge));
    color: var(--ink);
    text-align: center;
    padding-top: 62px;
  }
  .holder-name {
    font-size: 15px; font-weight: 700; letter-spacing: .5px;
    text-transform: uppercase;
  }
  .holder-title { font-size: 15px; margin-top: 2px; color: var(--ink-soft); }
  .profile-photo {
    width: 156px; height: 156px; border-radius: 50%;
    margin: 28px auto 0;
    border: 6px solid var(--photo-ring);
    background: radial-gradient(circle at 50% 38%, var(--photo-fill-a) 0 45%, var(--photo-fill-b) 100%);
  }
  .company-block { margin-top: 36px; font-size: 15px; line-height: 1.25; }
  .company-name { text-transform: uppercase; }
  .contact-icons {
    display: flex; justify-content: center; gap: 26px; margin-top: 34px;
  }
  .contact-icon {
    width: 30px; height: 30px; border-radius: 50%;
    background: var(--icon-bg);
    display: flex; align-items: center; justify-content: center;
  }
  .contact-icon svg { width: 16px; height: 16px; }
  .contact-lines { margin-top: 18px; font-size: 16px; line-height: 1.3; }
  /* Back */
  .card-back {
    background: linear-gradient(170deg, var(--back-top), var(--back-bottom));
  }
  .brand-mark {
    position: absolute; top: 220px; left: 0; right: 0;
    display: flex; align-items: center; justify-content: center; gap: 12px;
  }
  .brand-dot {
    width: 18px; height: 18px; border-radius: 50%;
    background: var(--brand-orange);
  }
  .brand-name {
    font-size: 34px; font-weight: 700; letter-spacing: 1px;
    color: var(--brand-blue); text-transform: uppercase;
  }
  .brand-url {
    position: absolute; bottom: 44px; left: 0; right: 0;
    text-align: center; font-size: 14px; color: var(--brand-blue);
  }
  .brand-url .url-name { color: var(--brand-orange); }
</style>
</head>
<body>
  <main class="card-set">
    <section class="card card-front">
      <p class="holder-name">Daniel Harrow</p>
      <p class="holder-title">President &amp; CEO</p>
      <div class="profile-photo" role="img" aria-label="Profile photo of the card holder"></div>
      <div class="company-block">
        <p class="company-name">Brightwell Workplace Services</p>
        <p>Fenwick Lodge, Mill Lane,</p>
        <p>Oakridge Wick, KT14 3WB</p>
      </div>
      <div class="contact-icons">
        <span class="contact-icon" aria-label="Phone">
          <svg viewBox="0 0 16 16"><path fill="#fff" d="M3.5 1.5l2.2 2.6-1.3 1.6c.8 1.9 2.1 3.2 4 4l1.6-1.3 2.6 2.2-1 2.1C7 12.6 3.4 9 1.4 2.5z"/></svg>
        </span>
        <span class="contact-icon" aria-label="Email">
          <svg viewBox="0 0 16 16"><rect x="1.5" y="3.5" width="13" height="9" fill="none" stroke="#fff" stroke-width="1.3"/><path d="M1.8 3.8L8 9l6.2-5.2" fill="none" stroke="#fff" stroke-width="1.3"/></svg>
        </span>
        <span class="contact-icon" aria-label="Website">
          <svg viewBox="0 0 16 16"><g fill="none" stroke="#fff" stroke-width="1.5" stroke-linecap="round"><path d="M7 9.5l-1.8 1.8a2 2 0 01-2.8-2.8L4.8 6"/><path d="M9 6.5l1.8-1.8a2 2 0 012.8 2.8L11.2 10"/><path d="M6 10l4-4"/></g></svg>
        </span>
      </div>
      <div class="contact-lines">
        <p>01-632-960-418</p>
        <p>contact@brightwellws.com</p>
        <p>www.brightwellws.com</p>
      </div>
    </section>

    <section class="card card-back">
      <div class="brand-mark">
        <span class="brand-dot"></span>
        <span class="brand-name">Brightwell</span>
      </div>
      <p class="brand-url">www.<span class="url-name">brightwellws</span>.com</p>
    </section>
  </main>
</body>
</html>
```